Dog Coat Drive for San Francisco Homeless Pets

- one page, full color, flyer to advertise a winter dog coat drive.- requesting use of an image of pit bull type or chihuahua type dog in a coat - 2 size versions - 8.5 inch by 11 inch to be printed and a square design to be posted on FB, Instagram and websites

Font styles to use
Serif
Sans Serif

Colors

Designer to choose colors to be used in the design.

```html
<!DOCTYPE html>
<html lang="en">
<head>
<meta charset="utf-8">
<title>Dog Coat Drive Flyer</title>
<link href="https://fonts.googleapis.com/css2?family=Open+Sans:wght@400;600;700;800&display=swap" rel="stylesheet">
<style>
  :root{
    --stage:#d9d9d9;
    --paper:#f4f4f4;
    --blue:#1c93d1;
    --ink:#1f1f1f;
    --muted:#333;
    --band:#000;
    --white:#fff;
  }
  *{box-sizing:border-box;margin:0;padding:0}
  html,body{width:900px;height:1200px;overflow:hidden;background:var(--stage);font-family:"Open Sans",Arial,sans-serif;color:var(--ink)}
  .flyer{position:absolute;left:73px;top:73px;width:755px;height:1067px;background:var(--paper)}
  .abs{position:absolute}
  .brand{left:20px;top:58px;font-size:16px;font-weight:600;color:var(--ink);line-height:1}
  .contact{right:37px;text-align:right;font-size:12px;line-height:15px;color:var(--ink)}
  .contact svg{position:absolute;right:-17px;top:2px}
  .photo{position:absolute}
  .photo-main{left:0;top:139px;width:405px;height:435px;background:linear-gradient(160deg,#3a4d5c,#e9e7e4 60%,#3b3b3b)}
  .photo-top{left:413px;top:139px;width:342px;height:212px;background:linear-gradient(135deg,#7a4a2a,#c0392b 55%,#a8683c)}
  .photo-bottom{left:413px;top:359px;width:342px;height:215px;background:linear-gradient(135deg,#3a4148,#9acd32 55%,#5a5a5a)}
  .headline{left:23px;top:592px;font-size:30px;font-weight:800;color:var(--blue);letter-spacing:.3px}
  .subbar{left:15px;top:633px;width:442px;height:32px;background:linear-gradient(90deg,#1a1a1a,#444);color:var(--white);font-size:19px;font-weight:400;line-height:32px;padding-left:9px;letter-spacing:.2px}
  .dates{left:24px;top:674px;font-size:15px;font-weight:600;color:var(--blue)}
  .ask{left:24px;top:695px;width:710px;font-size:11.5px;line-height:16px;color:var(--muted)}
  .tab{left:0;top:747px;width:239px;height:27px;background:var(--blue);color:var(--white);font-size:12.5px;line-height:27px;padding-left:24px;border-radius:0 14px 14px 0}
  .partner{position:absolute;font-size:12px;color:var(--ink)}
  .partner h3{font-size:16px;font-weight:400;line-height:22px;margin-bottom:0}
  .partner p{display:flex;align-items:center;gap:7px;height:23px}
  .divider{position:absolute;width:0;height:62px;border-left:1.5px dotted #777}
  .band{left:0;top:972px;width:755px;height:95px;background:var(--band)}
  .badge{position:absolute;top:11px;height:72px;background:var(--white)}
</style>
</head>
<body>
<main class="flyer">
  <header>
    <div class="abs brand">Cozy Paws Van</div>

    <div class="abs contact" style="top:40px">+1 415-555-0142
      <svg width="11" height="11" viewBox="0 0 12 12"><circle cx="6" cy="6" r="6" fill="var(--blue)"/><path d="M4 3l1 1.5-.7.8c.5 1 1.3 1.8 2.4 2.4l.8-.7L9 8l-.7 1c-2.5-.3-4.6-2.4-5-5z" fill="#fff"/></svg></div>
    <div class="abs contact" style="top:66px">www.cozypawsvan.org
      <svg width="11" height="11" viewBox="0 0 12 12"><circle cx="6" cy="6" r="6" fill="var(--blue)"/><circle cx="6" cy="6" r="3" fill="none" stroke="#fff"/></svg></div>
    <div class="abs contact" style="top:92px">2210 Harbor Lane, #412 (12,588.24 km)<br>94114 San Francisco, California
      <svg width="11" height="12" viewBox="0 0 12 14"><path d="M6 0a5 5 0 0 1 5 5c0 4-5 9-5 9S1 9 1 5a5 5 0 0 1 5-5z" fill="var(--blue)"/><circle cx="6" cy="5" r="2" fill="#fff"/></svg></div>
  </header>

  <div class="photo photo-main" role="img" aria-label="Small white long-haired dog wearing a striped sweater"></div>
  <div class="photo photo-top" role="img" aria-label="Pit bull type dog in a red fleece coat on a wooden deck"></div>
  <div class="photo photo-bottom" role="img" aria-label="Brown and white dog in a bright green reflective jacket on a sidewalk"></div>

  <h1 class="abs headline">BABY, IT’S COLD OUTSIDE!</h1>
  <h2 class="abs subbar">DOG COAT DRIVE FOR SF NAVIGATION CENTERS</h2>
  <p class="abs dates">FROM DECEMBER THROUGH FEBRUARY</p>
  <p class="abs ask">Please donate new &amp; gently used dog coats, sweaters and jackets for Navigation Center dogs whose owners are working to prevent &amp; end their homelessness</p>

  <div class="abs tab">Coat Drop Partners &amp; Locations</div>

  <svg width="0" height="0" style="position:absolute">
    <defs>
      <symbol id="icon-phone" viewBox="0 0 12 12"><circle cx="6" cy="6" r="6" fill="#1c93d1"/><path d="M4 3l1 1.5-.7.8c.5 1 1.3 1.8 2.4 2.4l.8-.7L9 8l-.7 1c-2.5-.3-4.6-2.4-5-5z" fill="#fff"/></symbol>
      <symbol id="icon-pin" viewBox="0 0 12 14"><path d="M6 0a5 5 0 0 1 5 5c0 4-5 9-5 9S1 9 1 5a5 5 0 0 1 5-5z" fill="#1c93d1"/><circle cx="6" cy="5" r="2" fill="#fff"/></symbol>
    </defs>
  </svg>

  <div class="partner" style="left:23px;top:783px"><h3>Bay City ACC</h3>
    <p><svg width="11" height="11"><use href="#icon-phone"/></svg>415-555-0187</p>
    <p><svg width="11" height="12"><use href="#icon-pin"/></svg>820 Mission Row</p></div>
  <div class="divider" style="left:230px;top:786px"></div>
  <div class="partner" style="left:293px;top:783px"><h3>The Pet Parlor</h3>
    <p><svg width="11" height="11"><use href="#icon-phone"/></svg>415-555-0123</p>
    <p><svg width="11" height="12"><use href="#icon-pin"/></svg>64 Cedar Street</p></div>
  <div class="divider" style="left:495px;top:786px"></div>
  <div class="partner" style="left:553px;top:783px"><h3>Hillside Pet Co.</h3>
    <p><svg width="11" height="11"><use href="#icon-phone"/></svg>415-555-0176</p>
    <p><svg width="11" height="12"><use href="#icon-pin"/></svg>930 Maple Street</p></div>

  <div class="partner" style="left:23px;top:877px"><h3>Sunny Paws Pet Services</h3>
    <p><svg width="11" height="11"><use href="#icon-phone"/></svg>650-555-0119</p>
    <p><svg width="11" height="12"><use href="#icon-pin"/></svg>45 Seaview Drive, Pacifica</p></div>
  <div class="divider" style="left:230px;top:880px"></div>
  <div class="partner" style="left:293px;top:877px"><h3>The Rover Center</h3>
    <p><svg width="11" height="11"><use href="#icon-phone"/></svg>650-555-0164</p>
    <p><svg width="11" height="12"><use href="#icon-pin"/></svg>702 Coastline Avenue, Pacifica</p></div>

  <footer class="abs band">
    <div class="badge" style="left:20px;width:113px"></div>
    <div class="badge" style="left:153px;width:113px"></div>
    <div class="badge" style="left:292px;width:113px"></div>
    <div class="badge" style="left:427px;width:313px"></div>
  </footer>
</main>
</body>
</html>
```